MSA Plans

I would like to rebuild my brochure for the 3 business plans that I currently offer my clients. I would like to make it look much more modern & attractive to clients when choosing one of our service plans. If we can stick to a tech theme that would be great. Message me for anymore information.

```html
<!DOCTYPE html>
<html lang="en">
<head>
<meta charset="utf-8">
<title>Managed Services Framework – Brochure Spreads</title>
<link rel="stylesheet" href="https://fonts.googleapis.com/css2?family=Montserrat:wght@500;600;700;800;900&family=Quicksand:wght@400;500;600;700&family=Oswald:wght@300;400&display=swap">
<style>
:root{
  --orange:#ef5b22;
  --orange-soft:#f37a3f;
  --black:#141414;
  --ink:#2b2b2b;
  --grey-band:#575757;
  --row-a:#f1f1f1;
  --row-b:#ffffff;
  --canvas:#8e8e8e;
  --green:#3cc24a;
  --red:#e0262b;
  --white:#ffffff;
}
*{box-sizing:border-box;margin:0;padding:0}
html,body{width:1200px;height:574px;overflow:hidden;background:var(--canvas)}
body{position:relative;font-family:"Quicksand",sans-serif;color:var(--ink)}
.page{position:absolute;top:27px;width:345px;height:503px;background:var(--white);overflow:hidden}
.page--cover{left:49px}
.page--msa{left:423px}
.page--cyber{left:805px}

/* ---------- cover ---------- */
.cover-photo{position:absolute;inset:0;background:linear-gradient(135deg,#e9e2d8 0%,#c9b7a1 35%,#8a6a52 65%,#3a2a22 100%)}
.cover-top{position:absolute;left:0;top:0;width:345px;height:90px}
.brand{position:absolute;display:flex;align-items:center;gap:6px}
.brand-mark{width:14px;height:14px;background:var(--orange)}
.brand-name{font-family:"Montserrat",sans-serif;font-weight:700;color:var(--orange);letter-spacing:2px}
.cover .brand{left:28px;top:16px}
.cover .brand-mark{width:18px;height:18px}
.cover .brand-name{font-size:19px}
.cover-title-block{position:absolute;left:0;top:295px;width:221px;height:132px}
.cover-title{position:absolute;left:22px;top:18px;font-family:"Montserrat",sans-serif;font-weight:900;color:var(--white);font-size:19.5px;line-height:23px;letter-spacing:1.6px}
.cover-sub{position:absolute;left:23px;top:88px;font-size:11.2px;line-height:14.5px;color:var(--white);font-weight:500}
.cover-version{position:absolute;left:234px;top:395px;font-family:"Oswald",sans-serif;font-weight:300;color:var(--white);font-size:13px;line-height:17px}
.cover-footer{position:absolute;left:0;top:427px;width:345px;height:76px}
.footer-text{position:absolute;left:0;width:100%;text-align:center}
.footer-company{font-family:"Montserrat",sans-serif;font-weight:700;color:var(--orange);font-size:8.4px;letter-spacing:.1px}
.footer-line{font-size:8px;color:var(--white);font-weight:500;display:flex;justify-content:center;gap:10px;margin-top:3px}
.footer-line span{display:inline-flex;align-items:center;gap:3px}
.ico{width:7px;height:7px;fill:var(--orange)}

/* ---------- inner pages ---------- */
.top-photo{position:absolute;left:0;top:0;width:345px}
.page--msa .top-photo{height:93px;background:linear-gradient(120deg,#6b5b52 0%,#3d3431 45%,#2b2523 100%)}
.page--cyber .top-photo{height:209px;background:linear-gradient(110deg,#2f3b44 0%,#5a4132 35%,#2a2a2e 65%,#1a1a1c 100%)}

.grid{position:absolute;left:26px;background:var(--white);box-shadow:0 1px 4px rgba(0,0,0,.25)}
.page--msa .grid{top:37px;width:296px}
.row{display:grid;align-items:center;font-size:6.1px;font-weight:500;color:var(--ink)}
.page--msa .row{grid-template-columns:148px 50px 42px 56px}
.row > *{display:flex;align-items:center;justify-content:center;height:100%;text-align:center}
.row > .label{justify-content:flex-start;text-align:left;padding-left:6px;gap:4px}
.item{height:13.2px}
.item:nth-child(odd){background:var(--row-a)}
.item:nth-child(even){background:var(--row-b)}
.item > *{border-right:1px solid #dcdcdc}
.item > *:last-child{border-right:none}
.section{height:15px;background:var(--grey-band);color:var(--white);font-weight:700;font-size:6.6px}
.section > *{border-right:1px solid #6c6c6c}
.head{height:15px;color:var(--white);font-weight:700;font-size:6.6px}
.head > *{background:var(--orange);height:100%}
.head > .tab{position:relative;border-left:1px solid var(--white)}
.head > .tab::before{content:"";position:absolute;left:-1px;right:0;top:-7px;height:8px;background:var(--orange);border-radius:4px 4px 0 0}
.head .label{font-size:6.8px}

.bullet{width:6px;height:6px;border:1px solid #777;border-radius:50%;position:relative;flex:none}
.bullet::after{content:"";position:absolute;left:1.4px;top:.6px;width:1.3px;height:2.2px;border:solid #777;border-width:0 .8px .8px 0;transform:rotate(45deg)}
.section .bullet,.head .bullet{border-color:var(--white)}
.section .bullet::after,.head .bullet::after{border-color:var(--white)}

.ok,.no{width:8px;height:8px;border-radius:50%;position:relative;display:inline-block}
.ok{background:var(--green)}
.ok::after{content:"";position:absolute;left:2.7px;top:1.2px;width:2px;height:3.8px;border:solid var(--white);border-width:0 1.2px 1.2px 0;transform:rotate(45deg)}
.no{background:var(--red)}
.no::before,.no::after{content:"";position:absolute;left:3.4px;top:1.5px;width:1.2px;height:5px;background:var(--white)}
.no::before{transform:rotate(45deg)}
.no::after{transform:rotate(-45deg)}

.price{position:absolute;background:var(--orange);color:var(--white);display:grid;font-size:6.6px;line-height:8.6px;font-weight:500;border-radius:0 0 4px 4px}
.price > *{display:flex;flex-direction:column;justify-content:center;align-items:center;border-left:1px solid rgba(255,255,255,.5)}
.price > .label{align-items:flex-end;padding-right:13px;border-left:none;text-align:right}
.page--msa .price{left:79px;top:389px;width:243px;height:34px;grid-template-columns:91px 50px 42px 60px}

/* cyber */
.page--cyber .grid{top:110px;width:295px}
.page--cyber .row{grid-template-columns:198px 41px 56px}
.page--cyber .item{height:12.8px}
.page--cyber .item.tall{height:25px;align-items:center}
.page--cyber .item.tall .label{align-items:flex-start;padding-top:3px}
.compliance{height:14px;background:var(--white);font-size:6.5px;border-bottom:3px solid #e3e3e3}
.compliance > *{border-right:1px solid #dcdcdc}
.compliance > *:last-child{border-right:none}
.page--cyber .price{left:79px;top:335px;width:242px;height:33px;grid-template-columns:145px 41px 56px}
.page--cyber .brand{left:88px;top:388px}
.page--cyber .brand-mark{width:20px;height:20px}
.page--cyber .brand-name{font-size:20px}

.inner-footer{position:absolute;left:0;bottom:0;width:345px;height:70px}
.inner-footer .footer-text{top:27px}
</style>
</head>
<body>

<!-- Cover -->
<section class="page page--cover cover">
  <div class="cover-photo" role="img" aria-label="Photo of hands typing on a laptop keyboard with glowing cyber security padlock and network icons"></div>

  <svg class="cover-top" viewBox="0 0 345 90" aria-hidden="true">
    <polygon points="0,0 241,0 190,55 0,55" fill="#ffffff"/>
    <polygon points="0,0 40,0 0,40" fill="#ef5b22"/>
    <polygon points="0,55 0,82 40,55" fill="#ef5b22"/>
    <polygon points="218,35 272,0 300,0 245,35" fill="#141414"/>
    <polyline points="28,74 45,74 95,55 198,55 226,24" fill="none" stroke="#ffffff" stroke-width=".8"/>
  </svg>
  <div class="brand"><span class="brand-mark"></span><span class="brand-name">NORTHGATE</span></div>

  <svg style="position:absolute;left:0;top:290px" width="345" height="140" viewBox="0 0 345 140" aria-hidden="true">
    <polygon points="0,5 175,5 221,40 221,137 0,137" fill="#ef5b22"/>
    <polyline points="70,3 175,3 217,36 217,132" fill="none" stroke="#ffffff" stroke-width=".7"/>
    <polygon points="221,137 345,137 345,115 300,90 260,95" fill="#2a2a2a" opacity=".75"/>
  </svg>
  <div class="cover-title-block">
    <h1 class="cover-title">MANAGED<br>SERVICES<br>FRAMEWORK</h1>
    <p class="cover-sub">Defining our services and how we<br>deliver these consistently to you</p>
  </div>
  <p class="cover-version">VERSION 1.0<br>UPDATED: APRIL 2024</p>

  <svg class="cover-footer" viewBox="0 0 345 76" aria-hidden="true">
    <rect width="345" height="76" fill="#141414"/>
    <polygon points="0,25 0,76 58,76" fill="#ef5b22"/>
    <polygon points="130,76 160,55 345,55 345,76" fill="#1f1f1f"/>
  </svg>
  <div class="footer-text" style="top:453px">
    <p class="footer-company">NORTHGATE IT SERVICES PTY LTD | ABN: 48 210 395 117</p>
    <p class="footer-line">
      <span><svg class="ico" viewBox="0 0 10 10"><path d="M2 1h2l1 2.5-1.3 1a5 5 0 0 0 2.6 2.6l1-1.3L9.8 7v2A1 1 0 0 1 9 10 9 9 0 0 1 0 1a1 1 0 0 1 1-1z"/></svg>1300 555 018</span>
      <span><svg class="ico" viewBox="0 0 10 10"><path d="M9.5.5 0 4.5l4.2 1.3L5.5 10z"/></svg>12/40 Harlow St, Brookvale, VIC, 3199</span>
    </p>
    <p class="footer-line">
      <span><svg class="ico" viewBox="0 0 10 10"><circle cx="5" cy="5" r="4.3" fill="none" stroke="#ef5b22" stroke-width="1"/><path d="M.7 5h8.6M5 .7c-2.4 2.4-2.4 6.2 0 8.6M5 .7c2.4 2.4 2.4 6.2 0 8.6" fill="none" stroke="#ef5b22" stroke-width=".8"/></svg>northgateit.com.au</span>
      <span><svg class="ico" viewBox="0 0 10 10"><rect x=".5" y="1.5" width="9" height="7" fill="none" stroke="#ef5b22"/><path d="M.5 1.5 5 5.5l4.5-4" fill="none" stroke="#ef5b22"/></svg>service@northgateit.com.au</span>
    </p>
  </div>
</section>

<!-- Managed services agreement -->
<section class="page page--msa">
  <div class="top-photo" role="img" aria-label="Photo of a technician with glasses working at a computer"></div>

  <div class="grid">
    <div class="row head"><span class="label"><i class="bullet"></i>Managed Services Agreement</span><span class="tab">Essential</span><span class="tab">Business</span><span class="tab">Professional</span></div>
    <div class="row section"><span class="label"><i class="bullet"></i>Support</span><span></span><span></span><span></span></div>
    <div>
      <div class="row item"><span class="label"><i class="bullet"></i>Unlimited Remote Support 7am to 6pm</span><span><i class="ok"></i></span><span><i class="ok"></i></span><span><i class="ok"></i></span></div>
      <div class="row item"><span class="label"><i class="bullet"></i>3rd Party Vendor Support</span><span><i class="ok"></i></span><span><i class="ok"></i></span><span><i class="ok"></i></span></div>
      <div class="row item"><span class="label"><i class="bullet"></i>Reactive Onsite Support 8am to 5pm</span><span>VIP Rates</span><span><i class="ok"></i></span><span><i class="ok"></i></span></div>
      <div class="row item"><span class="label"><i class="bullet"></i>After-Hours Support</span><span>VIP Rates</span><span>VIP Rates</span><span><i class="ok"></i></span></div>
    </div>
    <div class="row section"><span class="label"><i class="bullet"></i>Support</span><span></span><span></span><span></span></div>
    <div>
      <div class="row item"><span class="label"><i class="bullet"></i>Guaranteed SLA Response Times</span><span><i class="ok"></i></span><span><i class="ok"></i></span><span><i class="ok"></i></span></div>
      <div class="row item"><span class="label"><i class="bullet"></i>24x7 Website &amp; Infrastructure Monitoring</span><span><i class="ok"></i></span><span><i class="ok"></i></span><span><i class="ok"></i></span></div>
      <div class="row item"><span class="label"><i class="bullet"></i>Secure Web Content Filtering</span><span><i class="ok"></i></span><span><i class="ok"></i></span><span><i class="ok"></i></span></div>
      <div class="row item"><span class="label"><i class="bullet"></i>Backup Monitoring</span><span><i class="ok"></i></span><span><i class="ok"></i></span><span><i class="ok"></i></span></div>
      <div class="row item"><span class="label"><i class="bullet"></i>Operating System Patching &amp; Updating</span><span><i class="ok"></i></span><span><i class="ok"></i></span><span><i class="ok"></i></span></div>
      <div class="row item"><span class="label"><i class="bullet"></i>CEO / MD Home Tech Support</span><span><i class="ok"></i></span><span><i class="ok"></i></span><span><i class="ok"></i></span></div>
      <div class="row item"><span class="label"><i class="bullet"></i>Monthly Tech Site Visit</span><span><i class="no"></i></span><span>Quarterly</span><span>Monthly</span></div>
      <div class="row item"><span class="label"><i class="bullet"></i>Short Term Loan Equipment</span><span><i class="no"></i></span><span>1 Month</span><span>3 Months</span></div>
      <div class="row item"><span class="label"><i class="bullet"></i>Adds / Moves / Changes (Staff)</span><span><i class="ok"></i></span><span><i class="ok"></i></span><span><i class="ok"></i></span></div>
      <div class="row item"><span class="label"><i class="bullet"></i>Adds / Moves / Changes (Workstations)</span><span>VIP Rates</span><span>VIP Rates</span><span><i class="ok"></i></span></div>
    </div>
    <div class="row section"><span class="label"><i class="bullet"></i>Management</span><span></span><span></span><span></span></div>
    <div>
      <div class="row item"><span class="label"><i class="bullet"></i>Asset and Warranty Tracking &amp; Reporting</span><span><i class="ok"></i></span><span><i class="ok"></i></span><span><i class="ok"></i></span></div>
      <div class="row item"><span class="label"><i class="bullet"></i>Comprehensive IT Documentation</span><span><i class="ok"></i></span><span><i class="ok"></i></span><span><i class="ok"></i></span></div>
      <div class="row item"><span class="label"><i class="bullet"></i>Technology Strategy Meeting</span><span>Annual</span><span>Quarterly</span><span>Monthly</span></div>
      <div class="row item"><span class="label"><i class="bullet"></i>Technology Business Review Meeting</span><span>Annual</span><span>Bi Annual</span><span>Quarterly</span></div>
      <div class="row item"><span class="label"><i class="bullet"></i>IT Policy Templates</span><span><i class="no"></i></span><span><i class="ok"></i></span><span><i class="ok"></i></span></div>
    </div>
    <div class="row section"><span class="label"><i class="bullet"></i>Training</span><span></span><span></span><span></span></div>
    <div>
      <div class="row item"><span class="label"><i class="bullet"></i>End User Training Materials</span><span><i class="no"></i></span><span><i class="no"></i></span><span><i class="ok"></i></span></div>
      <div class="row item"><span class="label"><i class="bullet"></i>Security Awareness Training</span><span><i class="ok"></i></span><span><i class="ok"></i></span><span><i class="ok"></i></span></div>
    </div>
  </div>

  <div class="price">
    <div class="label"><span>RRP / User</span><span>Minimum User Count</span><span>Minimum Monthly Commit</span></div>
    <div><span>$110</span><span>5</span><span>$550</span></div>
    <div><span>$130</span><span>5</span><span>$650</span></div>
    <div><span>$165</span><span>5</span><span>$825</span></div>
  </div>

  <svg class="inner-footer" viewBox="0 0 345 70" aria-hidden="true">
    <polygon points="22,70 22,20 42,6 118,6 130,14 210,14 222,6 300,6 322,20 345,20 345,70" fill="#141414"/>
    <polygon points="0,70 0,30 22,30 22,70" fill="#141414"/>
    <polyline points="8,31 24,20" stroke="#ef5b22" stroke-width=".8"/>
    <polyline points="318,14 328,22" stroke="#ef5b22" stroke-width=".8"/>
  </svg>
  <div class="footer-text" style="top:458px">
    <p class="footer-company">NORTHGATE IT SERVICES PTY LTD | ABN: 48 210 395 117</p>
    <p class="footer-line">
      <span><svg class="ico" viewBox="0 0 10 10"><path d="M2 1h2l1 2.5-1.3 1a5 5 0 0 0 2.6 2.6l1-1.3L9.8 7v2A1 1 0 0 1 9 10 9 9 0 0 1 0 1a1 1 0 0 1 1-1z"/></svg>1300 555 018</span>
      <span><svg class="ico" viewBox="0 0 10 10"><path d="M9.5.5 0 4.5l4.2 1.3L5.5 10z"/></svg>12/40 Harlow St, Brookvale, VIC, 3199</span>
    </p>
    <p class="footer-line">
      <span><svg class="ico" viewBox="0 0 10 10"><circle cx="5" cy="5" r="4.3" fill="none" stroke="#ef5b22" stroke-width="1"/><path d="M.7 5h8.6M5 .7c-2.4 2.4-2.4 6.2 0 8.6M5 .7c2.4 2.4 2.4 6.2 0 8.6" fill="none" stroke="#ef5b22" stroke-width=".8"/></svg>northgateit.com.au</span>
      <span><svg class="ico" viewBox="0 0 10 10"><rect x=".5" y="1.5" width="9" height="7" fill="none" stroke="#ef5b22"/><path d="M.5 1.5 5 5.5l4.5-4" fill="none" stroke="#ef5b22"/></svg>service@northgateit.com.au</span>
    </p>
  </div>
</section>

<!-- Cybersecurity packages -->
<section class="page page--cyber">
  <div class="top-photo" role="img" aria-label="Photo of a businessman in a suit touching glowing orange cloud network and data icons"></div>

  <div class="grid">
    <div class="row head"><span class="label"><i class="bullet"></i>Cybersecurity Packages</span><span class="tab">Business</span><span class="tab">Professional</span></div>
    <div class="row compliance"><span class="label"><i class="bullet"></i>Compliance with National Essential 8 Maturity</span><span>Level 0</span><span>Level 1</span></div>
    <div>
      <div class="row item"><span class="label"><i class="bullet"></i>Security Standard - Alignment to Northgate Cloud Suite Security</span><span><i class="ok"></i></span><span><i class="ok"></i></span></div>
      <div class="row item"><span class="label"><i class="bullet"></i>Policy &amp; Reporting</span><span><i class="ok"></i></span><span><i class="ok"></i></span></div>
      <div class="row item"><span class="label"><i class="bullet"></i>24x7 Security Operations Centre (SOC) - Monitoring Cloud Suite</span><span><i class="ok"></i></span><span><i class="ok"></i></span></div>
      <div class="row item"><span class="label"><i class="bullet"></i>Dark Web Scanning</span><span><i class="ok"></i></span><span><i class="ok"></i></span></div>
      <div class="row item"><span class="label"><i class="bullet"></i>Cloud Email Filtering</span><span><i class="ok"></i></span><span><i class="ok"></i></span></div>
      <div class="row item"><span class="label"><i class="bullet"></i>Cloud Suite Backup</span><span><i class="ok"></i></span><span><i class="ok"></i></span></div>
      <div class="row item"><span class="label"><i class="bullet"></i>Automated Email Signatures</span><span><i class="ok"></i></span><span><i class="ok"></i></span></div>
      <div class="row item"><span class="label"><i class="bullet"></i>Endpoint Protection with EDR - Workstations &amp; Servers</span><span><i class="ok"></i></span><span><i class="ok"></i></span></div>
      <div class="row item"><span class="label"><i class="bullet"></i>3rd Party Applications Updating</span><span><i class="no"></i></span><span><i class="ok"></i></span></div>
      <div class="row item"><span class="label"><i class="bullet"></i>24x7 Security Operations Centre (SOC) - Monitoring</span><span><i class="no"></i></span><span><i class="ok"></i></span></div>
      <div class="row item"><span class="label"><i class="bullet"></i>Endpoints and Servers</span><span></span><span></span></div>
      <div class="row item"><span class="label"><i class="bullet"></i>Privileged Access Management &amp; Application Whitelisting</span><span><i class="no"></i></span><span><i class="ok"></i></span></div>
      <div class="row item"><span class="label"><i class="bullet"></i>Internal Vulnerability Scanning</span><span><i class="no"></i></span><span><i class="ok"></i></span></div>
      <div class="row item tall"><span class="label"><i class="bullet"></i>Backup &amp; Disaster Recovery to comply with National Essential<br>8 Maturity Level 1</span><span><i class="no"></i></span><span>Pending<br>Assessment</span></div>
    </div>
  </div>

  <div class="price">
    <div class="label"><span>RRP / User</span><span>Minimum User Count</span><span>Minimum Monthly Commit</span></div>
    <div><span>$35</span><span>5</span><span>$175</span></div>
    <div><span>$60</span><span>5</span><span>$300</span></div>
  </div>

  <div class="brand"><span class="brand-mark"></span><span class="brand-name">NORTHGATE</span></div>

  <svg class="inner-footer" viewBox="0 0 345 70" aria-hidden="true">
    <polygon points="22,70 22,20 42,6 118,6 130,14 210,14 222,6 300,6 322,20 345,20 345,70" fill="#141414"/>
    <polygon points="0,70 0,30 22,30 22,70" fill="#141414"/>
    <polyline points="8,31 24,20" stroke="#ef5b22" stroke-width=".8"/>
    <polyline points="318,14 328,22" stroke="#ef5b22" stroke-width=".8"/>
  </svg>
  <div class="footer-text" style="top:458px">
    <p class="footer-company">NORTHGATE IT SERVICES PTY LTD | ABN: 48 210 395 117</p>
    <p class="footer-line">
      <span><svg class="ico" viewBox="0 0 10 10"><path d="M2 1h2l1 2.5-1.3 1a5 5 0 0 0 2.6 2.6l1-1.3L9.8 7v2A1 1 0 0 1 9 10 9 9 0 0 1 0 1a1 1 0 0 1 1-1z"/></svg>1300 555 018</span>
      <span><svg class="ico" viewBox="0 0 10 10"><path d="M9.5.5 0 4.5l4.2 1.3L5.5 10z"/></svg>12/40 Harlow St, Brookvale, VIC, 3199</span>
    </p>
    <p class="footer-line">
      <span><svg class="ico" viewBox="0 0 10 10"><circle cx="5" cy="5" r="4.3" fill="none" stroke="#ef5b22" stroke-width="1"/><path d="M.7 5h8.6M5 .7c-2.4 2.4-2.4 6.2 0 8.6M5 .7c2.4 2.4 2.4 6.2 0 8.6" fill="none" stroke="#ef5b22" stroke-width=".8"/></svg>northgateit.com.au</span>
      <span><svg class="ico" viewBox="0 0 10 10"><rect x=".5" y="1.5" width="9" height="7" fill="none" stroke="#ef5b22"/><path d="M.5 1.5 5 5.5l4.5-4" fill="none" stroke="#ef5b22"/></svg>service@northgateit.com.au</span>
    </p>
  </div>
</section>

</body>
</html>
```